New business card for my lawn and landscape business

Dorrin Yard and Building is a full-service lawn care, landscaping, and light construction company serving Paragould and the the Maple Valley Region region. The business is owned and operated by Marcus Toller, with a reputation for hands-on, detail-oriented service, dependable crews, and quality results for both residential and commercial clients. A well regarded business with great reviews.
Owner Marcus Toller
Dorrinyardandbuilding.example

Target Market(s)

Commercial, Middle, and upper class in north east Arkansas

Industry/Entity Type

Lawn maintenance and landscape

Contact Information for Business Card

Dorrin Yard And Building Professional lawn care, landscaping, and property improvement in the Maple Valley Region. • lawn maintenance •lawn treatments and weed control • exterior projects • Custom landscape design & installation • Sod, trees, rock & drainage solutions • Residential & commercial services Reliable. Detailed. Done right.

Requirements
Must have
• Business name, service area, list of some of our services, clean design that represents
Nice to have
• Unique. Different design element than just grass because its already in n the logo. Picture of a warm season (south) lawn or landscape. Pictures of the type of work we do

```html
<!DOCTYPE html>
<html lang="en">
<head>
<meta charset="UTF-8">
<title>Dorrin Yard and Building – Business Card</title>
<link href="https://fonts.googleapis.com/css2?family=Montserrat:wght@600;700;800&family=Arimo:wght@400;700&display=swap" rel="stylesheet">
<style>
  :root {
    --stage: #2e2e2e;
    --card-black: #0d0d0d;
    --card-black-soft: #1e1e1e;
    --ring: #262626;
    --green: #7bc043;
    --green-dark: #5a9e34;
    --green-light: #8fcf4e;
    --white: #ffffff;
    --ink: #1a1a1a;
  }
  * { box-sizing: border-box; margin: 0; padding: 0; }
  html, body { width: 1200px; height: 800px; overflow: hidden; }
  body {
    background: var(--stage);
    display: flex;
    align-items: center;
    justify-content: center;
    gap: 36px;
    font-family: "Arimo", Arial, sans-serif;
  }
  .card {
    position: relative;
    width: 560px;
    height: 320px;
    border-radius: 18px;
    overflow: hidden;
    box-shadow: 0 14px 30px rgba(0,0,0,.45);
  }

  /* Front */
  .card-front {
    background: radial-gradient(circle at 20% 30%, var(--card-black-soft), var(--card-black) 70%);
  }
  .brand {
    display: flex;
    align-items: center;
    gap: 10px;
    font-family: "Montserrat", sans-serif;
    font-weight: 700;
    color: var(--green);
  }
  .brand-dot {
    width: 26px; height: 26px; border-radius: 50%;
    background: var(--green);
    flex: none;
  }
  .card-front .brand {
    position: absolute;
    left: 30px; top: 132px;
    font-size: 17px;
    line-height: 1.15;
    width: 200px;
  }
  .dark-ring {
    position: absolute;
    right: 0; top: -14px;
    width: 346px; height: 348px;
    background: var(--ring);
    border-radius: 174px 0 0 174px;
  }
  .green-panel {
    position: absolute;
    right: 0; top: 0;
    width: 330px; height: 320px;
    background: linear-gradient(160deg, var(--green-light), var(--green-dark));
    border-radius: 160px 0 0 160px;
    color: var(--white);
    text-align: right;
    padding: 32px 34px 0 0;
  }
  .phone {
    display: flex; justify-content: flex-end; align-items: center; gap: 8px;
    font-weight: 700; font-size: 16px;
  }
  .owner-name {
    margin-top: 62px;
    font-family: "Montserrat", sans-serif;
    font-weight: 800;
    font-size: 30px;
    letter-spacing: .5px;
    line-height: 1.1;
  }
  .owner-title { font-size: 15px; margin-top: 4px; letter-spacing: .5px; }
  .address { margin-top: 50px; font-size: 14px; font-weight: 700; line-height: 1.3; }

  /* Back */
  .card-back { background: var(--white); color: var(--ink); padding: 26px 30px; }
  .back-head { display: flex; justify-content: space-between; align-items: flex-start; }
  .card-back .brand { font-size: 13px; width: 160px; line-height: 1.15; }
  .contact { list-style: none; font-size: 13px; text-align: right; line-height: 1.6; }
  .contact li { display: flex; justify-content: flex-end; align-items: center; gap: 6px; }
  .company-title {
    margin-top: 22px;
    font-family: "Montserrat", sans-serif;
    font-weight: 700;
    font-size: 23px;
    color: var(--green);
    letter-spacing: 1px;
  }
  .intro { margin-top: 8px; font-size: 13.5px; line-height: 1.3; }
  .services { list-style: none; margin-top: 4px; font-size: 13.5px; line-height: 1.32; }
  .services li::before { content: "•"; color: var(--green); font-weight: 700; margin-right: 7px; }
</style>
</head>
<body>

<section class="card card-front" aria-label="Business card front">
  <div class="brand"><span class="brand-dot"></span><span>Dorrin Yard and Building</span></div>
  <div class="dark-ring"></div>
  <div class="green-panel">
    <p class="phone">
      <svg width="12" height="18" viewBox="0 0 12 18" aria-hidden="true"><rect x="1" y="1" width="10" height="16" rx="2" fill="none" stroke="#fff" stroke-width="1.8"/><line x1="4.5" y1="14" x2="7.5" y2="14" stroke="#fff" stroke-width="1.6"/></svg>
      (870) 555-0148
    </p>
    <h1 class="owner-name">MARCUS TOLLER</h1>
    <p class="owner-title">OWNER</p>
    <p class="address">Millbrook, MV, United<br>States, Maple Valley</p>
  </div>
</section>

<section class="card card-back" aria-label="Business card back">
  <div class="back-head">
    <div class="brand"><span class="brand-dot"></span><span>Dorrin Yard and Building</span></div>
    <ul class="contact">
      <li>
        <svg width="13" height="13" viewBox="0 0 14 14" aria-hidden="true"><path d="M1 7 L13 1 L8 13 L7 8 Z" fill="var(--green)"/></svg>
        hello@dorrinyardandbuilding.example
      </li>
      <li>
        <svg width="13" height="13" viewBox="0 0 14 14" aria-hidden="true"><circle cx="7" cy="7" r="6" fill="var(--green)"/><path d="M1 7 H13 M7 1 C4 4 4 10 7 13 M7 1 C10 4 10 10 7 13" stroke="#fff" stroke-width="1" fill="none"/></svg>
        www.dorrinyardandbuilding.example
      </li>
    </ul>
  </div>
  <h2 class="company-title">DORRIN YARD AND BUILDING</h2>
  <p class="intro">Dorrin Yard And Building Professional lawn care<br>Landscaping and property improvement in the Maple Valley Region</p>
  <ul class="services">
    <li>Lawn maintenance</li>
    <li>Lawn treatments and weed control</li>
    <li>Exterior projects</li>
    <li>Custom landscape design &amp; installation</li>
    <li>Sod, trees, rock &amp; drainage solutions</li>
    <li>Residential &amp; commercial services Reliable</li>
  </ul>
</section>

</body>
</html>
```